Golden Coat All-Purpose Breading Bag Design

Our client, Harlow Food Products, is looking to re-design the packaging for their product, Pellworth's Golden Coat. Goldn Coat is an all-purpose food breading mix.

Harlow Foods has a registered trademark for this product, but they have not been using it for this particular 10 pound bag. They want to get the trademark onto the bag and also give the bag an updated look. They would like to continue to use the same red and blue colors. This 10 pound bag is not available on store shelves; it is sold to food service distributors who sell to restaurants.

All of the copy on the existing bag is still relevant, so we will want to incoprporate it into the bag design. Once these bags are filled with product, the tops get folded over about 1 inch and then sewn shut with thread.

Eventually, we will need the design applied to the Bag Template file attached, but that isn't important until a design is selected.

Target Market(s)

Restaurants

Industry/Entity Type

Food Manufacturing

Colors
0054AA
0677BA
7BADD7
CADEEF
E8F1F8
EB3D1F
EC4F4E
F09395
F8D3D4
FCEDEE

Requirements
Must have
• Trademark introduced to the design

```html
<!DOCTYPE html>
<html lang="en">
<head>
<meta charset="utf-8">
<title>Pellworth's Golden Coat – 10 lb Bag Dieline</title>
<link rel="stylesheet" href="https://fonts.googleapis.com/css2?family=Open+Sans:wght@400;600;700;800&display=swap">
<style>
  :root {
    --backdrop: #646464;
    --paper: #ffffff;
    --navy: #2c2a6f;
    --crimson: #a71f24;
  }
  * { margin: 0; padding: 0; box-sizing: border-box; }
  html, body { width: 720px; height: 1200px; overflow: hidden; }
  body {
    background: var(--backdrop);
    font-family: "Open Sans", sans-serif;
    color: var(--navy);
    position: relative;
  }
  .dieline { position: absolute; left: 20px; top: 340px; width: 681px; height: 522px; }
  .dieline__body { position: absolute; left: 0; top: 0; width: 681px; height: 422px; background: var(--paper); }
  .dieline__flap {
    position: absolute; left: 141px; top: 422px; width: 178px; height: 100px;
    background: var(--paper);
    display: flex; flex-direction: column; align-items: center; justify-content: center;
    font-size: 5.6px; font-weight: 700; line-height: 12px; text-align: center;
  }
  .panel { position: absolute; top: 0; height: 422px; }
  .panel--side-left { left: 0; width: 114px; }
  .panel--front { left: 114px; width: 233px; }
  .panel--side-right { left: 347px; width: 106px; }
  .panel--back { left: 453px; width: 228px; }

  .wordmark { position: absolute; font-weight: 800; line-height: 1; }
  .wordmark__owner { display: block; }
  .wordmark__product { display: block; }
  .wordmark sup { font-size: 0.45em; vertical-align: top; margin-left: 2px; }
  .wordmark--small { left: 14px; top: 112px; width: 80px; color: var(--crimson); }
  .wordmark--small .wordmark__owner { font-size: 7px; margin-bottom: 3px; }
  .wordmark--small .wordmark__product { font-size: 17px; }
  .wordmark--large { left: 33px; top: 72px; width: 170px; }
  .wordmark--large .wordmark__owner { font-size: 13px; margin-bottom: 6px; }
  .wordmark--large .wordmark__product { font-size: 34px; }
  .wordmark--navy { color: var(--navy); }
  .wordmark--red { color: var(--crimson); }

  .side-heading { position: absolute; left: 0; width: 100%; text-align: center; font-weight: 700; }
  .side-copy {
    position: absolute; font-size: 7.6px; line-height: 9.9px; text-align: justify;
    hyphens: manual;
  }
  .side-copy p + p { margin-top: 9px; }

  .panel--side-left .side-heading { top: 186px; font-size: 10px; }
  .panel--side-left .side-copy { left: 14px; top: 203px; width: 92px; }

  .panel--side-right .side-heading--main { top: 183px; font-size: 13px; line-height: 19px; font-weight: 800; }
  .panel--side-right .side-heading--sub { top: 223px; font-size: 9.5px; }
  .panel--side-right .side-copy { left: 9px; top: 252px; width: 87px; font-size: 8.2px; line-height: 12.3px; }

  .band { position: absolute; color: #fff; text-align: center; }
  .band--maker { left: 33px; top: 191px; width: 166px; height: 50px; background: var(--crimson); padding-top: 11px; }
  .band--maker .band__title { font-size: 8.6px; font-weight: 700; }
  .band--maker .band__line { font-size: 5.8px; font-weight: 600; line-height: 8px; }
  .band--claims { left: 5px; top: 261px; width: 221px; height: 110px; background: var(--navy); padding-top: 12px; }
  .band--claims .band__title { font-size: 11.5px; font-weight: 700; margin-bottom: 4px; }
  .band--claims .band__note { font-size: 5.6px; line-height: 10px; }
  .band--claims .band__slogan { font-size: 8.8px; font-weight: 700; line-height: 12px; margin-top: 3px; }
  .band--claims .band__ingredients { font-size: 5.4px; font-weight: 600; line-height: 8px; margin-top: 12px; }
  .net-weight { position: absolute; left: 0; top: 385px; width: 100%; text-align: center; font-size: 11px; font-weight: 700; }

  .band--method { left: 35px; top: 193px; width: 166px; height: 74px; background: var(--navy); padding-top: 15px; }
  .band--method .band__title { font-size: 12px; font-weight: 700; line-height: 15px; }
  .band--method .band__title em { font-size: 9px; font-style: normal; font-weight: 600; }
  .band--method .band__note { font-size: 5.6px; font-weight: 600; margin-top: 4px; }
  .band--uses { left: 35px; top: 273px; width: 166px; height: 78px; background: var(--crimson); padding-top: 11px; }
  .band--uses .band__line { font-size: 7.6px; font-weight: 700; line-height: 15.6px; letter-spacing: 0.3px; }
</style>
</head>
<body>
  <main class="dieline">
    <div class="dieline__body">

      <section class="panel panel--side-left">
        <div class="wordmark wordmark--small">
          <span class="wordmark__owner">Pellworth's</span>
          <span class="wordmark__product">Golden Coat<sup>®</sup></span>
        </div>
        <h2 class="side-heading">PELLWORTH'S</h2>
        <div class="side-copy">
          <p>Golden Coat is a prepared formula of pure foods that enables you to fry chicken from the raw to the well done in ten minutes. It seals in all the natural juice and creates a very thin crunchy coating which the fat does not pene&shy;trate – thereby using much less fat than ordi&shy;nary frying methods.</p>
          <p>This formula is an all-dry mix to be used on any&shy;thing breaded – fish, oys&shy;ters, shrimp, veal and chicken fried steak.</p>
        </div>
      </section>

      <section class="panel panel--front">
        <div class="wordmark wordmark--large wordmark--navy">
          <span class="wordmark__owner">Pellworth's</span>
          <span class="wordmark__product">Golden Coat<sup>®</sup></span>
        </div>
        <div class="band band--maker">
          <div class="band__title">by HARLOW FOOD PRODUCTS</div>
          <div class="band__line">418 ORCHARD LANE</div>
          <div class="band__line">CEDAR FALLS, OHIO 44021</div>
        </div>
        <div class="band band--claims">
          <div class="band__title">THE ALL PURPOSE BREADING</div>
          <div class="band__note">SEALS JUICE IN GREASE OUT</div>
          <div class="band__note">Cooks two-pound chicken well done in 10 minutes (deep fat).</div>
          <div class="band__slogan">Chicken fried the GOLDEN COAT way<br>is fried chicken the right way.</div>
          <div class="band__ingredients">INGREDIENTS: FLOUR, SALT, NON-FAT MILK SOLIDS, EGG YOLK,<br>BAKING POWDER, CORN STARCH, SUGAR AND PEPPER.</div>
        </div>
        <div class="net-weight">NET WT. 10 LBS.</div>
      </section>

      <section class="panel panel--side-right">
        <div class="wordmark wordmark--small">
          <span class="wordmark__owner">Pellworth's</span>
          <span class="wordmark__product">Golden Coat<sup>®</sup></span>
        </div>
        <h2 class="side-heading side-heading--main">NOTHING<br>TO ADD</h2>
        <h3 class="side-heading side-heading--sub">DIRECTIONS</h3>
        <div class="side-copy">
          <p>Wet all foods in water, then place in dry dip, coating thoroughly. Fry (350° F.) chicken 1 ½ to 2# 10 minutes, over 2# slightly longer. For best re&shy;sults double dip onion rings and oysters.</p>
        </div>
      </section>

      <section class="panel panel--back">
        <div class="wordmark wordmark--large wordmark--red">
          <span class="wordmark__owner">Pellworth's</span>
          <span class="wordmark__product">Golden Coat<sup>®</sup></span>
        </div>
        <div class="band band--method">
          <div class="band__title"><em>for</em> DEEP FAT<br><em>and</em> PAN FRYING</div>
          <div class="band__note">(SLIGHTLY LONGER ON PAN FRYING)</div>
        </div>
        <div class="band band--uses">
          <div class="band__line">OF CHICKEN . STEAKS . CHOPS</div>
          <div class="band__line">TENDERLOIN . FISH . SHRIMP</div>
          <div class="band__line">OYSTERS &amp; OTHER SEA FOODS</div>
          <div class="band__line">ONION RINGS &amp; VEGETABLES</div>
        </div>
      </section>

    </div>
    <div class="dieline__flap">
      <span>CHICKEN FRIED THE GOLDEN COAT WAY</span>
      <span>IS FRIED CHICKEN THE RIGHT WAY.</span>
    </div>
  </main>
</body>
</html>
```